Coral Journey Mate - A Travel Services Website

Sunreef Home Rentals is a company that provides travels services to home owners and travellers to Barbados. Coral Journey Mate is a particular brand targeting travelling guests with specific set of travel services. The brand slogan is:

'Getting you the best for less'

The travel services will include:

- Coral Journey Mate Perks Pass
- Car Hire Quote Service
- Mobile Phone Sim Cards
- Prepaid Debit Cards
- Airport Hotel Booking
- Airport Lounge Booking
- Airport Parking

There will also be a travel planner function for guests.

The main puropse of the site is as follows:

1. Registration for the Coral Journey Mate Perks Pass

2. Creation of user account which the guest will frequently return to check for updates

3. Purchase of ancillary travel products and services

4. To use the Travel Planner

5. To gather data on holiday home owners in Barbados

A site map can be seen at the following link:

http://plotgridly.example/outlines/viewMap/4kqzvbn8ytrwpa2fuh5ximc07jldg6sqenoa9rvb33kf2pyq71

Webpage templates (2 required)

The first will be form control heavy (text boxes, checkboxes ect). It will need failure and success messages / indicators etc.

The second will be a general content area with a secondary navigation area (i.e for sub sections of the current section). This will house text / headings and images.

Both will require header, primary navigation, content and footer areas.

N.B. Please not that I am not technical and the above webtemplate narrative has been supplied by my web developer/programmer. If you have any questions, please ask me any questions and I will get an answer from him.

Target Market(s)

My customers tend to be:

Sex: Female
Age: 24-55
Location: UK, USA, Canada
Social Class: A,B,C1
Income: Medium income bracket

They are possibly visiting Barbados for the first and only time. It is an expensive destination and is accessible to people with a medium to high income. They still desire 'value for money'. Therefore the sight must give guests confidence that Coral Journey Mate is 'their friend', is seeking to offer the best value deals for their vacation/holiday.

Industry/Entity Type

Travel

Requirements
Must have
• The site templates must be professional, aspirational, trustworthy, reassuring, clean, innovative, fun. When people visit the site they should be excited about the savings that they can make and want to return as there is a perceived benefit for them. It must look expensive and professional in its projected image.
Nice to have
• Smooth currved lines, seperated boxed areas for content, as simple and uncluttered layout and it must be simple to read!
Should not have
• It should not be cartoonly, despite my attached logo and must not look cheap.

```html
<!DOCTYPE html>
<html lang="en">
<head>
<meta charset="utf-8">
<title>Coral Journey Mate – Car Hire Dashboard</title>
<link href="https://fonts.googleapis.com/css2?family=Open+Sans:ital,wght@0,400;0,600;0,700;1,600&display=swap" rel="stylesheet">
<style>
:root{
  --brand-pink:#d8336e;
  --nav-grey:#6b6b6b;
  --sky-top:#5fa6dc;
  --sea:#2bb3c4;
  --sea-deep:#1a8fa8;
  --sand:#e9e1cf;
  --leaf-dark:#1f4a2a;
  --panel:rgba(255,255,255,0.94);
  --panel-head:#3c4a55;
  --rule:#d9dde0;
  --text:#4a4a4a;
  --muted:#7a7a7a;
  --label:#2a6fa3;
  --white:#ffffff;
}
*{box-sizing:border-box;margin:0;padding:0}
html,body{width:1200px;height:1095px;overflow:hidden}
body{font-family:"Open Sans",Arial,sans-serif;color:var(--text);position:relative;
  background:linear-gradient(180deg,#7fb9d8 480px,#4d8a56 620px,var(--leaf-dark) 1000px);}
.site-header{position:absolute;left:0;top:0;width:1200px;height:84px;background:var(--white)}
.brand{position:absolute;left:40px;top:20px;display:flex;align-items:center;gap:10px}
.brand-dot{width:30px;height:30px;border-radius:50%;background:var(--brand-pink)}
.brand-name{font-size:26px;font-weight:700;color:var(--brand-pink);line-height:1}
.primary-nav{position:absolute;right:30px;top:36px;display:flex;font-size:12.5px;color:var(--nav-grey)}
.primary-nav a{color:inherit;text-decoration:none;padding:0 9px;border-left:1px solid #bbb}
.primary-nav a:first-child{border-left:0}
.hero{position:absolute;left:0;top:84px;width:1200px;height:420px;
  background:linear-gradient(180deg,var(--sky-top) 0%,#9fd0ea 38%,var(--sea) 60%,var(--sea-deep) 80%,var(--sand) 100%)}
.hero-title{position:absolute;left:42px;top:80px;width:370px;color:var(--white);font-size:22px;font-weight:700;line-height:1.25}
.hero-copy{position:absolute;left:42px;top:178px;width:262px;color:var(--white);font-size:10.5px;line-height:1.5}
.photo-line{position:absolute;left:0;top:84px}
.polaroid{position:absolute;width:110px;height:120px;background:var(--white);padding:7px 7px 20px;box-shadow:0 3px 8px rgba(0,0,0,.3)}
.polaroid .shot{width:100%;height:100%}
.dashboard{position:absolute;left:165px;top:485px;width:1020px;height:505px;background:var(--panel);border-radius:10px;box-shadow:0 4px 14px rgba(0,0,0,.25)}
.dash-head{position:absolute;left:20px;top:12px;width:980px;height:36px;background:var(--panel-head);border-radius:6px 6px 0 0;color:var(--white);padding:4px 0 0 110px;font-size:13px;line-height:1.2}
.dash-head small{display:block;font-size:10px;opacity:.85}
.tabs{position:absolute;left:140px;top:62px;font-size:12.5px;font-weight:600;color:#333;display:flex;gap:18px}
.side-note{position:absolute;left:22px;top:92px;width:110px;border:1px solid var(--rule);background:#fff;padding:6px;font-size:9.5px;color:var(--muted);line-height:1.35}
.side-note strong{color:var(--label)}
.quote-table{position:absolute;left:140px;top:88px;width:870px;border-collapse:collapse;font-size:10.5px}
.quote-table td{vertical-align:top;padding:5px 6px;border-bottom:1px solid var(--rule);line-height:1.45}
.quote-table .group{color:var(--label);font-style:italic;font-weight:600;width:150px}
.quote-table .group::before{content:"";display:inline-block;width:6px;height:6px;border-radius:50%;background:var(--label);margin-right:6px;vertical-align:middle}
.actions a{color:#222;font-weight:700;text-decoration:none;margin-right:8px}
.site-footer{position:absolute;left:0;top:1005px;width:1200px;height:90px;background:rgba(16,36,47,.92);color:var(--white);font-size:12px;line-height:1.5}
.site-footer h2{font-size:14px;font-weight:700;margin-bottom:8px}
.foot-address{position:absolute;left:30px;top:12px}
.foot-phone{position:absolute;left:470px;top:38px}
.foot-web{position:absolute;right:40px;top:38px;text-align:right}
</style>
</head>
<body>
<header class="site-header">
  <div class="brand"><span class="brand-dot"></span><span class="brand-name">Coral Journey Mate</span></div>
  <nav class="primary-nav">
    <a href="#">Home</a><a href="#">Airport Parking</a><a href="#">Airport Hotel</a><a href="#">Airport Lounge</a><a href="#">Car Hire</a><a href="#">Attractions</a><a href="#">Travel Money</a><a href="#">Mobile Simcards</a><a href="#">Perks Pass</a>
  </nav>
</header>

<section class="hero" role="img" aria-label="Tropical beach with turquoise sea and blue sky">
  <h1 class="hero-title">Fill the Coral Journey Mate form with your personal details to hire a car</h1>
  <p class="hero-copy">Plan your island stay with ease and let us handle the small details for you. Share your travel dates, where you wish to collect your car and where you will return it, and we will send you several quotes from trusted local hire firms. Compare the offers side by side, choose the one that suits you and confirm it from your account dashboard whenever you are ready to book. Every quote stays saved so you can return and review it at any time.</p>
</section>

<svg class="photo-line" width="1200" height="260" viewBox="0 0 1200 260" aria-hidden="true">
  <path d="M330 175 Q 750 150 1195 215" fill="none" stroke="#ffffff" stroke-width="1.5" opacity=".8"/>
</svg>

<div class="polaroid" style="left:335px;top:258px;transform:rotate(-6deg)"><div class="shot" role="img" aria-label="Holiday photo of a sandy beach" style="background:linear-gradient(#8fc9e3,#e6d6b3)"></div></div>
<div class="polaroid" style="left:465px;top:250px;transform:rotate(4deg)"><div class="shot" role="img" aria-label="Holiday photo of a palm-lined shore" style="background:linear-gradient(#4aa7c9,#5d8f4f)"></div></div>
<div class="polaroid" style="left:595px;top:255px;transform:rotate(-3deg)"><div class="shot" role="img" aria-label="Holiday photo of a beach cove" style="background:linear-gradient(#6fc0da,#d8c9a4)"></div></div>
<div class="polaroid" style="left:730px;top:262px;transform:rotate(5deg)"><div class="shot" role="img" aria-label="Holiday photo of clear shallow water" style="background:linear-gradient(#7ccfe0,#2d9fb5)"></div></div>
<div class="polaroid" style="left:870px;top:270px;transform:rotate(-4deg)"><div class="shot" role="img" aria-label="Holiday photo of a seaside view" style="background:linear-gradient(#9cd3ea,#e3d9c0)"></div></div>
<div class="polaroid" style="left:1015px;top:282px;transform:rotate(3deg)"><div class="shot" role="img" aria-label="Holiday photo of a boat on the sea" style="background:linear-gradient(#5db5d6,#1d7f99)"></div></div>

<main class="dashboard">
  <div class="dash-head">Account Dashboard:<small>XXXX XXXXXX</small></div>
  <div class="tabs"><span>Car Hire</span><span>» Request prices</span></div>
  <aside class="side-note"><strong>Note</strong><br>Manage your quotes and bookings here</aside>
  <table class="quote-table">
    <tr><td class="group">Open Quotes</td><td>Pick Up Location Date<br>Harbour Inn<br>05/01/2011</td><td>Drop Off Location Date<br>Airport<br>01/02/2011</td><td>Driver's Age<br>32</td><td>Car Group<br>Economy</td><td>Your Currency<br>English Pounds</td><td class="actions"><br><a href="#">View</a><a href="#">Cancel</a></td></tr>
    <tr><td class="group">Accepted Quotes</td><td>Pick Up Location Date<br>Southampton<br>13/02/2011</td><td>Drop Off Location Date<br>Florida<br>11/01/2011</td><td>Driver's Age<br>22</td><td>Car Group<br>Mini Economy</td><td>Your Currency<br>English Pounds</td><td class="actions"><br><a href="#">View</a><a href="#">Cancel</a></td></tr>
    <tr><td class="group">Confirm Bookings</td><td>Pick Up Location Date<br>Bay Hotel<br>16/01/2011</td><td>Drop Off Location Date<br>Airport<br>12/01/2011</td><td>Driver's Age<br>41</td><td>Car Group<br>Compact</td><td>Your Currency<br>English Pounds</td><td class="actions"><br><a href="#">View</a></td></tr>
    <tr><td></td><td>Airport<br>09/04/2011</td><td>Hotel<br>18/04/2011</td><td>28</td><td>Economy</td><td>English Pounds</td><td class="actions"><a href="#">View</a></td></tr>
    <tr><td></td><td>Hotel Ocean<br>13/01/2011</td><td>Reef Beach<br>20/01/2011</td><td>35</td><td>Large Family</td><td>English Pounds</td><td class="actions"><a href="#">View</a></td></tr>
    <tr><td></td><td>Main Street<br>11/10/2011</td><td>Harbour<br>14/10/2011</td><td>47</td><td>People Carrier</td><td>English Pounds</td><td class="actions"><a href="#">View</a></td></tr>
  </table>
</main>

<div class="polaroid" style="left:150px;top:780px;transform:rotate(-8deg)"><div class="shot" role="img" aria-label="Holiday snapshot of the coast" style="background:linear-gradient(#8ecbe3,#d9cba8)"></div></div>
<div class="polaroid" style="left:200px;top:800px;transform:rotate(5deg)"><div class="shot" role="img" aria-label="Holiday snapshot of a beach" style="background:linear-gradient(#5fb6d3,#e5dcc4)"></div></div>

<footer class="site-footer">
  <div class="foot-address"><h2>Contact Us:</h2>Harbour Lane House, 12 Palm Row, Seaside Parish,<br>BB00000</div>
  <div class="foot-phone">Telephone: (246) 555-0142 | (246) 555-0187<br>Fax: (246) 555-0199</div>
  <div class="foot-web">www.coraljourneymate.example<br>hello@coraljourneymate.example</div>
</footer>
</body>
</html>
```